REDESIGN SIGN UP PAGE - EASY TO READ AND UNDERSTAND QUICKLY

I need to redesign my sign up page DESKTOP AND MOBILE VERSION to include 2 products that are each available as a monthly subscription, 6 mth or 12 mth subscription.

Currently I only promote one product on my website but now will be two. https://www.brightlanerewardhub.biz/signup

Now I will have two products:

1. UNLIMITED VACATION CERTIFICATES, DINING VOUCHERS & SAVINGS INCENTIVES
Unlimited Monthly Plan $99 / Month + $199 One-Time Set-Up Fee
Unlimited Bi Annual Plan $490 / 6 Months + $199 One-Time Set-Up Fee
Unlimited Annual Plan $898 / 12 Months + $199 One-Time Set-Up Fee

2. UNLIMITED SMART DEVICE INCENTIVES & OTHER HARD PREMIUMS
Unlimited Monthly Plan $299 / Month + $199 One-Time Set-Up Fee
Unlimited Bi Annual Plan $1,590 / 6 Months + $199 One-Time Set-Up Fee
Unlimited Annual Plan $2,898 / 12 Months + $199 One-Time Set-Up Fee

When promoting the different plans you can see the different categories of incentives I offer here: https://www.brightlanerewardhub.biz/incentives

The SMART DEVICE CERTIFICATES & INCENTIVES category is for product #2 and all the rest of the Categories is for Product #1 Feel free to use images as a visual so customers can see that this product includes Vacations & Restaurants and this product includes only smart devices....

USE ALL CURRENT BULLET POINTS FOR BOTH PLANS THAT IS CURRENTLY ON WEBSITE. USE ALL CURRENT CONTENT ON WEBSITE ORIGINAL SIGN UP PAGE. DO NOT LEAVE ANY CONTENT OUT.

Target Market(s)

BUSINESS OWNERS

Industry/Entity Type

Marketing

Number of Pages Required

2 page

Requirements
Must have
• When promoting the 2 different products on the new sign up page you can see the different categories of incentives I offer here: https://www.brightlanerewardhub.biz/incentives fee; free to use images to showcase what each product offers.

The SMART DEVICE CERTIFICATES & INCENTIVES category is for product #2 and all the rest of the Categories is for Product #1

I want the user to easily understand we have two products that are available in 3 ways, monthly subscription, bi annual and annual and can see the price immediately for all 3 options for both products without toggling, etc.

Must be super clean easy to ready design. Not too busy at all please
Nice to have
• USE ALL CURRENT BULLET POINTS FOR BOTH PLANS THAT IS CURRENTLY ON WEBSITE. USE ALL CURRENT CONTENT ON WEBSITE ORIGINAL SIGN UP PAGE. DO NOT LEAVE ANY CONTENT OUT.

Should not have

```html
<!DOCTYPE html>
<html lang="en">
<head>
<meta charset="utf-8">
<title>Sign Up – Brightlane Reward Hub</title>
<link href="https://fonts.googleapis.com/css2?family=Poppins:wght@400;500;600;700;800&family=Rubik:wght@400;500&display=swap" rel="stylesheet">
<style>
:root{
  --blue:#1656b0;
  --blue-dark:#0f479c;
  --green:#43b02a;
  --green-dark:#36971f;
  --ink:#1b1c20;
  --text:#3c3f46;
  --muted:#7b7f88;
  --line:#e6e8ec;
  --navy:#1c2330;
  --charcoal:#363a43;
  --hl-lime:#8fd63a;
  --hl-gold:#f8c21e;
  --hl-orange:#f79a1e;
}
*{box-sizing:border-box;margin:0;padding:0}
html,body{width:1200px;height:3361px;overflow:hidden;background:#fff}
body{font-family:'Poppins',sans-serif;color:var(--text);position:relative}
ul{list-style:none}

/* header */
.topbar{position:absolute;left:0;top:0;width:1200px;height:63px;background:#fff}
.brand{position:absolute;left:18px;top:0;height:63px;display:flex;align-items:center;gap:10px;font-weight:600;font-size:21px;color:var(--blue)}
.brand-dot{width:16px;height:16px;border-radius:50%;background:var(--blue)}
.mainnav{position:absolute;left:333px;top:0;width:554px;height:63px;background:var(--blue);clip-path:polygon(0 0,100% 0,100% 100%,24px 100%,0 0%,16px 50%);display:flex;align-items:center;padding-left:50px;gap:18px}
.mainnav{clip-path:polygon(0 0,100% 0,100% 100%,0 100%,22px 50%)}
.mainnav a{color:#fff;font-size:11.5px;text-decoration:none;font-weight:500}
.account{position:absolute;top:0;height:63px;display:flex;flex-direction:column;align-items:center;justify-content:center;color:#fff;font-size:11px;gap:3px}
.account.login{left:887px;width:85px;background:var(--charcoal)}
.account.signup{left:972px;width:45px;width:45px;background:var(--blue-dark);font-size:10px;white-space:nowrap}
.account.signup{left:951px;width:66px}
.account.login{width:64px}
.callbox{position:absolute;left:1017px;top:0;width:183px;height:63px;background:var(--green);display:flex;align-items:center;gap:8px;padding-left:16px;color:#fff;font-size:9.5px;font-weight:600;line-height:1.55}

/* plan sections */
.plan-section{position:absolute;left:0;width:1200px}
.plan-section.vacation{top:63px;height:1430px}
.plan-section.devices{top:1493px;height:1425px;border-top:1px solid var(--line)}
.section-icon{position:absolute;left:532px;width:136px;height:136px;border-radius:50%;border:5px solid #e9ecf1;box-shadow:0 2px 6px rgba(0,0,0,.12)}
.vacation .section-icon{top:52px;background:var(--blue)}
.devices .section-icon{top:30px;background:var(--green)}
.section-title{position:absolute;left:0;width:1200px;text-align:center;font-weight:600;font-size:38px;letter-spacing:.5px;color:var(--ink);line-height:1}
.section-sub{position:absolute;left:0;width:1200px;text-align:center;font-weight:500;font-size:24px;letter-spacing:.4px;line-height:1}
.vacation .section-title{top:218px}
.vacation .section-sub{top:272px;color:var(--blue)}
.devices .section-title{top:196px}
.devices .section-sub{top:250px;color:var(--green)}

.plans{position:absolute;left:13px;width:1174px;display:flex;gap:30px}
.vacation .plans{top:352px}
.devices .plans{top:330px}
.plan-card{position:relative;width:371px;height:1007px;border:2px solid #eceef2;border-radius:10px;background:#fff;box-shadow:0 3px 8px rgba(0,0,0,.08);overflow:hidden}
.plan-head{height:70px;display:flex;align-items:center;justify-content:center;font-family:'Rubik',sans-serif;font-size:24px;color:#fff}
.vacation .plan-head{background:var(--blue)}
.devices .plan-head{background:var(--green)}
.hl-lime{color:var(--hl-lime)}
.hl-gold{color:var(--hl-gold)}
.hl-orange{color:var(--hl-orange)}
.price{position:absolute;top:92px;left:0;width:100%;text-align:center;color:var(--ink);white-space:nowrap}
.price .cur{font-size:26px;vertical-align:top;position:relative;top:4px;color:#444}
.price .amt{font-size:76px;font-weight:600;line-height:1;letter-spacing:-1px}
.price .per{font-size:21px;color:var(--muted)}
.setup{position:absolute;top:170px;left:0;width:100%;text-align:center;font-size:15px;font-weight:500}
.vacation .setup{color:var(--blue)}
.devices .setup{color:var(--green)}
.plan-card hr{position:absolute;left:0;width:100%;border:0;border-top:1px solid var(--line)}
.hr-top{top:216px}
.hr-bottom{top:918px}
.features{position:absolute;top:236px;left:0;width:100%}
.features li{height:35.2px;display:flex;align-items:center;font-size:12.6px;color:var(--text);padding-left:22px;gap:16px;white-space:nowrap}
.tick{width:12px;height:12px;flex:none}
.vacation .tick{color:var(--blue)}
.devices .tick{color:var(--green)}
.select-btn{position:absolute;top:939px;left:97px;width:176px;height:47px;border-radius:24px;display:flex;align-items:center;justify-content:center;gap:10px;color:#fff;font-size:16px;font-weight:500}
.vacation .select-btn{background:var(--blue)}
.devices .select-btn{background:var(--green)}

/* footer */
.site-footer{position:absolute;left:0;top:2918px;width:1200px;height:443px;background:var(--navy);color:#c4cad6;font-size:11.4px}
.foot-brand{position:absolute;left:100px;top:85px;width:230px;display:flex;align-items:center;justify-content:center;gap:8px;font-size:19px;font-weight:600;color:var(--blue);color:#2f7ae0}
.foot-brand .brand-dot{background:#2f7ae0}
.social{position:absolute;left:129px;top:152px;display:flex;gap:10px}
.social span{width:36px;height:36px;border-radius:50%;background:#5a6170}
.samples-btn{position:absolute;left:102px;top:219px;width:224px;height:52px;border-radius:4px;background:var(--green);color:#fff;text-align:center;font-weight:800;font-size:13.5px;line-height:1.1;padding-top:11px;letter-spacing:-.2px}
.samples-btn small{display:block;font-weight:500;font-size:11px;margin-top:2px}
.foot-col{position:absolute;top:55px}
.foot-col h4{font-size:14.5px;font-weight:800;color:#fff;letter-spacing:-.3px;margin-bottom:24px}
.contact{left:377px;width:290px}
.contact .row{display:flex;gap:8px;margin-bottom:10px;line-height:1.45}
.contact .ic{width:14px;height:14px;flex:none;margin-top:2px;color:#8a92a3}
.contact b{color:#fff;font-weight:600}
.contact .green{color:var(--green)}
.quick{left:698px;width:170px}
.other{left:889px;width:220px}
.foot-col li{margin-bottom:8.5px;line-height:1.45}
.copyright{position:absolute;left:100px;top:403px;font-size:11.6px;color:#8a92a3}
.copyright b{color:#fff;font-weight:600}
.copyright .blue{color:#2f7ae0}
.legal{position:absolute;left:876px;top:403px;font-size:11.6px;color:#8a92a3}
</style>
</head>
<body>

<header class="topbar">
  <div class="brand"><span class="brand-dot"></span>Brightlane Reward Hub</div>
  <nav class="mainnav">
    <a>Home</a><a>The Incentives</a><a>Samples</a><a>Industries</a><a>Testimonials</a><a>Faq</a><a>Integrations</a>
  </nav>
  <div class="account login">
    <svg width="14" height="14" viewBox="0 0 16 16" fill="#fff"><circle cx="8" cy="5" r="3.5"/><path d="M1 16c0-4 3-6.5 7-6.5s7 2.5 7 6.5z"/></svg>LOGIN
  </div>
  <div class="account signup">
    <svg width="14" height="14" viewBox="0 0 16 16" fill="none" stroke="#fff" stroke-width="1.6"><circle cx="8" cy="8" r="6.5"/><path d="M8 11V5M5.5 7.5 8 5l2.5 2.5"/></svg>SIGN UP
  </div>
  <div class="callbox">
    <svg width="16" height="28" viewBox="0 0 16 28" fill="none" stroke="#fff" stroke-width="2"><rect x="1" y="1" width="14" height="26" rx="2"/><path d="M6 23h4"/></svg>
    <div>CALL US: 1-555-010-4821<br>TEXT US: 1-555-010-7730</div>
  </div>
</header>

<svg width="0" height="0" style="position:absolute">
  <symbol id="tick" viewBox="0 0 12 12"><circle cx="6" cy="6" r="5" fill="none" stroke="currentColor" stroke-width="1.6"/><path d="M3.8 6.1 5.4 7.6 8.3 4.6" fill="none" stroke="currentColor" stroke-width="1.6"/></symbol>
  <symbol id="arrow" viewBox="0 0 14 14"><circle cx="7" cy="7" r="6" fill="none" stroke="#fff" stroke-width="1.6"/><path d="M4 7h5M7 4.8 9.2 7 7 9.2" fill="none" stroke="#fff" stroke-width="1.6"/></symbol>
</svg>

<section class="plan-section vacation">
  <div class="section-icon" role="img" aria-label="Beach umbrella and lounge chair icon"></div>
  <h1 class="section-title">UNLIMITED VACATION CERTIFICATES,</h1>
  <h2 class="section-sub">DINING VOUCHERS &amp; SAVINGS INCENTIVES</h2>
  <div class="plans">
    <article class="plan-card">
      <div class="plan-head">Unlimited&nbsp;<span class="hl-lime">Monthly</span>&nbsp;Plan</div>
      <div class="price"><span class="cur">$</span><span class="amt">99</span><span class="per">/mo</span></div>
      <p class="setup">$199 One-Time Set-Up Fee</p>
      <hr class="hr-top">
      <ul class="features">
        <li><svg class="tick"><use href="#tick"/></svg>Unlimited E-Certificates</li>
        <li><svg class="tick"><use href="#tick"/></svg>Unlimited SMS Certificates</li>
        <li><svg class="tick"><use href="#tick"/></svg>Unlimited Web Banner Certificates</li>
        <li><svg class="tick"><use href="#tick"/></svg>Unlimited White Label Certificate Landing Pages</li>
        <li><svg class="tick"><use href="#tick"/></svg>Unlimited Website Sticky Bar Certificates</li>
        <li><svg class="tick"><use href="#tick"/></svg>Unlimited Website Pop Up Certificate</li>
        <li><svg class="tick"><use href="#tick"/></svg>Unlimited API E-Certificates</li>
        <li><svg class="tick"><use href="#tick"/></svg>Unlimited FlowBridge Integration Access</li>
        <li><svg class="tick"><use href="#tick"/></svg>FREE Warm Lead Letter Templates</li>
        <li><svg class="tick"><use href="#tick"/></svg>FREE Customer Appreciation Letter Templates</li>
        <li><svg class="tick"><use href="#tick"/></svg>FREE Professional-Grade Incentive Videos</li>
        <li><svg class="tick"><use href="#tick"/></svg>FREE Proven Social Media Ad Templates</li>
        <li><svg class="tick"><use href="#tick"/></svg>FREE High-Converting Banner Ad Templates</li>
        <li><svg class="tick"><use href="#tick"/></svg>FREE Time-Tested Print Ad Templates</li>
        <li><svg class="tick"><use href="#tick"/></svg>FREE White Label Redemption Website</li>
        <li><svg class="tick"><use href="#tick"/></svg>FREE Industry Specific Ad Packs</li>
        <li><svg class="tick"><use href="#tick"/></svg>FREE Affiliate Program-Earn 50% Commissions</li>
        <li><svg class="tick"><use href="#tick"/></svg>FREE Eye-Catching Posters, Flyers &amp; Brochures</li>
        <li><svg class="tick"><use href="#tick"/></svg>FREE Step by Step Redemption Guides</li>
      </ul>
      <hr class="hr-bottom">
      <div class="select-btn">Select <svg width="14" height="14"><use href="#arrow"/></svg></div>
    </article>
    <article class="plan-card">
      <div class="plan-head">Unlimited&nbsp;<span class="hl-gold">Bi Annual</span>&nbsp;Plan</div>
      <div class="price"><span class="cur">$</span><span class="amt">490</span><span class="per">/6mo</span></div>
      <p class="setup">$199 One-Time Set-Up Fee</p>
      <hr class="hr-top">
      <ul class="features">
        <li><svg class="tick"><use href="#tick"/></svg>Unlimited E-Certificates</li>
        <li><svg class="tick"><use href="#tick"/></svg>Unlimited SMS Certificates</li>
        <li><svg class="tick"><use href="#tick"/></svg>Unlimited Web Banner Certificates</li>
        <li><svg class="tick"><use href="#tick"/></svg>Unlimited White Label Certificate Landing Pages</li>
        <li><svg class="tick"><use href="#tick"/></svg>Unlimited Website Sticky Bar Certificates</li>
        <li><svg class="tick"><use href="#tick"/></svg>Unlimited Website Pop Up Certificate</li>
        <li><svg class="tick"><use href="#tick"/></svg>Unlimited API E-Certificates</li>
        <li><svg class="tick"><use href="#tick"/></svg>Unlimited FlowBridge Integration Access</li>
        <li><svg class="tick"><use href="#tick"/></svg>FREE Warm Lead Letter Templates</li>
        <li><svg class="tick"><use href="#tick"/></svg>FREE Customer Appreciation Letter Templates</li>
        <li><svg class="tick"><use href="#tick"/></svg>FREE Professional-Grade Incentive Videos</li>
        <li><svg class="tick"><use href="#tick"/></svg>FREE Proven Social Media Ad Templates</li>
        <li><svg class="tick"><use href="#tick"/></svg>FREE High-Converting Banner Ad Templates</li>
        <li><svg class="tick"><use href="#tick"/></svg>FREE Time-Tested Print Ad Templates</li>
        <li><svg class="tick"><use href="#tick"/></svg>FREE White Label Redemption Website</li>
        <li><svg class="tick"><use href="#tick"/></svg>FREE Industry Specific Ad Packs</li>
        <li><svg class="tick"><use href="#tick"/></svg>FREE Affiliate Program-Earn 50% Commissions</li>
        <li><svg class="tick"><use href="#tick"/></svg>FREE Eye-Catching Posters, Flyers &amp; Brochures</li>
        <li><svg class="tick"><use href="#tick"/></svg>FREE Step by Step Redemption Guides</li>
      </ul>
      <hr class="hr-bottom">
      <div class="select-btn">Select <svg width="14" height="14"><use href="#arrow"/></svg></div>
    </article>
    <article class="plan-card">
      <div class="plan-head">Unlimited&nbsp;<span class="hl-orange">Annual</span>&nbsp;Plan</div>
      <div class="price"><span class="cur">$</span><span class="amt">898</span><span class="per">/12mo</span></div>
      <p class="setup">$199 One-Time Set-Up Fee</p>
      <hr class="hr-top">
      <ul class="features">
        <li><svg class="tick"><use href="#tick"/></svg>Unlimited E-Certificates</li>
        <li><svg class="tick"><use href="#tick"/></svg>Unlimited SMS Certificates</li>
        <li><svg class="tick"><use href="#tick"/></svg>Unlimited Web Banner Certificates</li>
        <li><svg class="tick"><use href="#tick"/></svg>Unlimited White Label Certificate Landing Pages</li>
        <li><svg class="tick"><use href="#tick"/></svg>Unlimited Website Sticky Bar Certificates</li>
        <li><svg class="tick"><use href="#tick"/></svg>Unlimited Website Pop Up Certificate</li>
        <li><svg class="tick"><use href="#tick"/></svg>Unlimited API E-Certificates</li>
        <li><svg class="tick"><use href="#tick"/></svg>Unlimited FlowBridge Integration Access</li>
        <li><svg class="tick"><use href="#tick"/></svg>FREE Warm Lead Letter Templates</li>
        <li><svg class="tick"><use href="#tick"/></svg>FREE Customer Appreciation Letter Templates</li>
        <li><svg class="tick"><use href="#tick"/></svg>FREE Professional-Grade Incentive Videos</li>
        <li><svg class="tick"><use href="#tick"/></svg>FREE Proven Social Media Ad Templates</li>
        <li><svg class="tick"><use href="#tick"/></svg>FREE High-Converting Banner Ad Templates</li>
        <li><svg class="tick"><use href="#tick"/></svg>FREE Time-Tested Print Ad Templates</li>
        <li><svg class="tick"><use href="#tick"/></svg>FREE White Label Redemption Website</li>
        <li><svg class="tick"><use href="#tick"/></svg>FREE Industry Specific Ad Packs</li>
        <li><svg class="tick"><use href="#tick"/></svg>FREE Affiliate Program-Earn 50% Commissions</li>
        <li><svg class="tick"><use href="#tick"/></svg>FREE Eye-Catching Posters, Flyers &amp; Brochures</li>
        <li><svg class="tick"><use href="#tick"/></svg>FREE Step by Step Redemption Guides</li>
      </ul>
      <hr class="hr-bottom">
      <div class="select-btn">Select <svg width="14" height="14"><use href="#arrow"/></svg></div>
    </article>
  </div>
</section>

<section class="plan-section devices">
  <div class="section-icon" role="img" aria-label="Home and smartphone device icon"></div>
  <h1 class="section-title">UNLIMITED SMART DEVICE INCENTIVES</h1>
  <h2 class="section-sub">&amp; OTHER HARD PREMIUMS</h2>
  <div class="plans">
    <article class="plan-card">
      <div class="plan-head">Unlimited&nbsp;<span class="hl-gold">Monthly</span>&nbsp;Plan</div>
      <div class="price"><span class="cur">$</span><span class="amt">299</span><span class="per">/mo</span></div>
      <p class="setup">$199 One-Time Set-Up Fee</p>
      <hr class="hr-top">
      <ul class="features">
        <li><svg class="tick"><use href="#tick"/></svg>Unlimited E-Certificates</li>
        <li><svg class="tick"><use href="#tick"/></svg>Unlimited SMS Certificates</li>
        <li><svg class="tick"><use href="#tick"/></svg>Unlimited Web Banner Certificates</li>
        <li><svg class="tick"><use href="#tick"/></svg>Unlimited White Label Certificate Landing Pages</li>
        <li><svg class="tick"><use href="#tick"/></svg>Unlimited Website Sticky Bar Certificates</li>
        <li><svg class="tick"><use href="#tick"/></svg>Unlimited Website Pop Up Certificate</li>
        <li><svg class="tick"><use href="#tick"/></svg>Unlimited API E-Certificates</li>
        <li><svg class="tick"><use href="#tick"/></svg>Unlimited FlowBridge Integration Access</li>
        <li><svg class="tick"><use href="#tick"/></svg>FREE Warm Lead Letter Templates</li>
        <li><svg class="tick"><use href="#tick"/></svg>FREE Customer Appreciation Letter Templates</li>
        <li><svg class="tick"><use href="#tick"/></svg>FREE Professional-Grade Incentive Videos</li>
        <li><svg class="tick"><use href="#tick"/></svg>FREE Proven Social Media Ad Templates</li>
        <li><svg class="tick"><use href="#tick"/></svg>FREE High-Converting Banner Ad Templates</li>
        <li><svg class="tick"><use href="#tick"/></svg>FREE Time-Tested Print Ad Templates</li>
        <li><svg class="tick"><use href="#tick"/></svg>FREE White Label Redemption Website</li>
        <li><svg class="tick"><use href="#tick"/></svg>FREE Industry Specific Ad Packs</li>
        <li><svg class="tick"><use href="#tick"/></svg>FREE Affiliate Program-Earn 50% Commissions</li>
        <li><svg class="tick"><use href="#tick"/></svg>FREE Eye-Catching Posters, Flyers &amp; Brochures</li>
        <li><svg class="tick"><use href="#tick"/></svg>FREE Step by Step Redemption Guides</li>
      </ul>
      <hr class="hr-bottom">
      <div class="select-btn">Select <svg width="14" height="14"><use href="#arrow"/></svg></div>
    </article>
    <article class="plan-card">
      <div class="plan-head">Unlimited&nbsp;<span class="hl-orange">Bi Annual</span>&nbsp;Plan</div>
      <div class="price"><span class="cur">$</span><span class="amt">1590</span><span class="per">/6mo</span></div>
      <p class="setup">$199 One-Time Set-Up Fee</p>
      <hr class="hr-top">
      <ul class="features">
        <li><svg class="tick"><use href="#tick"/></svg>Unlimited E-Certificates</li>
        <li><svg class="tick"><use href="#tick"/></svg>Unlimited SMS Certificates</li>
        <li><svg class="tick"><use href="#tick"/></svg>Unlimited Web Banner Certificates</li>
        <li><svg class="tick"><use href="#tick"/></svg>Unlimited White Label Certificate Landing Pages</li>
        <li><svg class="tick"><use href="#tick"/></svg>Unlimited Website Sticky Bar Certificates</li>
        <li><svg class="tick"><use href="#tick"/></svg>Unlimited Website Pop Up Certificate</li>
        <li><svg class="tick"><use href="#tick"/></svg>Unlimited API E-Certificates</li>
        <li><svg class="tick"><use href="#tick"/></svg>Unlimited FlowBridge Integration Access</li>
        <li><svg class="tick"><use href="#tick"/></svg>FREE Warm Lead Letter Templates</li>
        <li><svg class="tick"><use href="#tick"/></svg>FREE Customer Appreciation Letter Templates</li>
        <li><svg class="tick"><use href="#tick"/></svg>FREE Professional-Grade Incentive Videos</li>
        <li><svg class="tick"><use href="#tick"/></svg>FREE Proven Social Media Ad Templates</li>
        <li><svg class="tick"><use href="#tick"/></svg>FREE High-Converting Banner Ad Templates</li>
        <li><svg class="tick"><use href="#tick"/></svg>FREE Time-Tested Print Ad Templates</li>
        <li><svg class="tick"><use href="#tick"/></svg>FREE White Label Redemption Website</li>
        <li><svg class="tick"><use href="#tick"/></svg>FREE Industry Specific Ad Packs</li>
        <li><svg class="tick"><use href="#tick"/></svg>FREE Affiliate Program-Earn 50% Commissions</li>
        <li><svg class="tick"><use href="#tick"/></svg>FREE Eye-Catching Posters, Flyers &amp; Brochures</li>
        <li><svg class="tick"><use href="#tick"/></svg>FREE Step by Step Redemption Guides</li>
      </ul>
      <hr class="hr-bottom">
      <div class="select-btn">Select <svg width="14" height="14"><use href="#arrow"/></svg></div>
    </article>
    <article class="plan-card">
      <div class="plan-head">Unlimited&nbsp;<span class="hl-gold">Annual</span>&nbsp;Plan</div>
      <div class="price"><span class="cur">$</span><span class="amt">2898</span><span class="per">/12mo</span></div>
      <p class="setup">$199 One-Time Set-Up Fee</p>
      <hr class="hr-top">
      <ul class="features">
        <li><svg class="tick"><use href="#tick"/></svg>Unlimited E-Certificates</li>
        <li><svg class="tick"><use href="#tick"/></svg>Unlimited SMS Certificates</li>
        <li><svg class="tick"><use href="#tick"/></svg>Unlimited Web Banner Certificates</li>
        <li><svg class="tick"><use href="#tick"/></svg>Unlimited White Label Certificate Landing Pages</li>
        <li><svg class="tick"><use href="#tick"/></svg>Unlimited Website Sticky Bar Certificates</li>
        <li><svg class="tick"><use href="#tick"/></svg>Unlimited Website Pop Up Certificate</li>
        <li><svg class="tick"><use href="#tick"/></svg>Unlimited API E-Certificates</li>
        <li><svg class="tick"><use href="#tick"/></svg>Unlimited FlowBridge Integration Access</li>
        <li><svg class="tick"><use href="#tick"/></svg>FREE Warm Lead Letter Templates</li>
        <li><svg class="tick"><use href="#tick"/></svg>FREE Customer Appreciation Letter Templates</li>
        <li><svg class="tick"><use href="#tick"/></svg>FREE Professional-Grade Incentive Videos</li>
        <li><svg class="tick"><use href="#tick"/></svg>FREE Proven Social Media Ad Templates</li>
        <li><svg class="tick"><use href="#tick"/></svg>FREE High-Converting Banner Ad Templates</li>
        <li><svg class="tick"><use href="#tick"/></svg>FREE Time-Tested Print Ad Templates</li>
        <li><svg class="tick"><use href="#tick"/></svg>FREE White Label Redemption Website</li>
        <li><svg class="tick"><use href="#tick"/></svg>FREE Industry Specific Ad Packs</li>
        <li><svg class="tick"><use href="#tick"/></svg>FREE Affiliate Program-Earn 50% Commissions</li>
        <li><svg class="tick"><use href="#tick"/></svg>FREE Eye-Catching Posters, Flyers &amp; Brochures</li>
        <li><svg class="tick"><use href="#tick"/></svg>FREE Step by Step Redemption Guides</li>
      </ul>
      <hr class="hr-bottom">
      <div class="select-btn">Select <svg width="14" height="14"><use href="#arrow"/></svg></div>
    </article>
  </div>
</section>

<footer class="site-footer">
  <div class="foot-brand"><span class="brand-dot"></span>Brightlane Reward Hub</div>
  <div class="social"><span></span><span></span><span></span><span></span></div>
  <div class="samples-btn">GET FREE SAMPLES<small>100% FREE</small></div>

  <div class="foot-col contact">
    <h4>CONTACT US</h4>
    <div class="row"><svg class="ic" viewBox="0 0 14 14" fill="none" stroke="currentColor" stroke-width="1.3"><path d="M7 13s4.5-4.2 4.5-7.5a4.5 4.5 0 0 0-9 0C2.5 8.8 7 13 7 13z"/><circle cx="7" cy="5.5" r="1.6"/></svg>
      <div><b>Brightlane Reward Group, Inc.</b><br>1450 Harbor Crest Drive Suite 210<br>Bayview, CA 90000</div></div>
    <div class="row"><svg class="ic" viewBox="0 0 14 14" fill="none" stroke="currentColor" stroke-width="1.3"><path d="M3 1.5h2.5l1 3-1.5 1a7 7 0 0 0 3.5 3.5l1-1.5 3 1V11a1.5 1.5 0 0 1-1.5 1.5A10 10 0 0 1 1.5 3 1.5 1.5 0 0 1 3 1.5z"/></svg>
      <div>USA Office: <b>1-555-010-4821</b><br>International: <b>1-800-555-0146</b><br>Text Us: <b>1-555-010-2290</b></div></div>
    <div class="row"><svg class="ic" viewBox="0 0 14 14" fill="none" stroke="currentColor" stroke-width="1.3"><rect x="1" y="3" width="12" height="8.5" rx="1"/><path d="M1 3.5 7 8l6-4.5"/></svg>
      <div>info@brightlanerewardhub.biz</div></div>
    <div class="row"><svg class="ic" viewBox="0 0 14 14" fill="none" stroke="currentColor" stroke-width="1.3"><circle cx="7" cy="7" r="5.8"/><path d="M7 3.8V7l2.2 1.4"/></svg>
      <div>24/7 Chat Support<br>24/7 Live Answering Service<br>24/7 Email Support<br><span class="green">Live Phone &amp; SMS Support:</span><br>Monday - Friday 8am - 5pm PST<br><span class="green">Sat/Sun/Holidays Closed</span></div></div>
  </div>

  <div class="foot-col quick">
    <h4>QUICK LINKS</h4>
    <ul>
      <li>Home</li><li>The Incentives</li><li>Samples</li><li>Affiliate</li><li>Testimonials</li><li>Faq</li><li>Contact Us</li><li>Redemption Demo Videos</li><li>Brightlane Distribute Certificate Demo Videos</li>
    </ul>
  </div>

  <div class="foot-col other">
    <h4>OTHER LINKS</h4>
    <ul>
      <li>Hoteliers</li><li>Brightlane Certificates List</li><li>How To Use Brightlane Certificates</li><li>Social Incentive Campaign</li><li>Pop Ups &amp; Sticky Bars</li><li>Whitepaper - Increase Sales</li><li>Whitepaper - Improve Sales During Strange Times</li><li>Whitepaper - Boost Website Conversions</li>
    </ul>
  </div>

  <p class="copyright">© 2020 <b>Brightlane Reward Group, Inc.</b> All Rights Reserved. CST# 4402187 <span class="blue">TCRC#</span> 736204</p>
  <p class="legal">Privacy Policy &nbsp;|&nbsp; Term And Conditions</p>
</footer>

</body>
</html>
```